Baby Cloth Business Needs a Web Design

We need a web design for a new company that produces and sells baby sleeping bags. We use brixVendor (demo.brixvendor.net) e-commerce software which we need a new design for that represents our products better. We would like to see designs that use simple and clean elements, playful layout with big pictures and emphasis on typography. We already have a logo that is "fresh" apple green so we would like colors that go well with that.
We use the following pages/features:
- Home page (with newsletter, chatterly link and contact us link)
- Category page (no search needed)
- Product details page (with share)
- User pages (register, login, my account)
- Shopping cart with all its pages (about 6-7)
- Static pages (3 pages: contact us, about us, conditions of use).

We need designs in the form of PSD

Target Market(s)

Primary: mothers 25-45; secondary: women 20-60 who buy it as gift

Industry/Entity Type

Business

Requirements
Must have
• Since the site uses brixVendor no other data can be added beside those already exist on site.
Nice to have
• We have photos taken for this site (sample attached) and would be nice to show them in big sizes. We would like to see imaginative, playful elements that appear several places throughout the site. Logo contains a small baby foot which could leave footprints here and there.

We like these sites (and what):
- http://www.plovik.net/13-organic-bamboo-cotton-baby-essentials (simple, nice but too gray)
- http://www.trelmark.net/ (logo placement, menu, background)
- http://www.zorpeli.net/
- http://www.qeb.net/website-template/view/html/baby-clothes?originUrl=http%3A%2F%2Fwww.qeb.net%2Fwebsite%2Ftemplates%2Fhtml%2Fonline-shop%2F2&galleryDocIndex=0 (layout, image sizes)
- http://themes.fashion.brix-layouts.net/?isOpen=false&;t_r=true (layout)
Should not have
• We do not use forum, blog, new products, manufacturers, popular tags, polls, search from brixVendor.

```html
<!DOCTYPE html>
<html lang="en">
<head>
<meta charset="utf-8">
<title>Dozelle – Sleeping bags for babies and kids</title>
<link rel="stylesheet" href="https://fonts.googleapis.com/css2?family=PT+Sans+Narrow:wght@400;700&family=PT+Sans:ital,wght@0,400;0,700;1,700&display=swap">
<style>
  :root {
    --slate: #2e3a40;
    --slate-deep: #263137;
    --green: #7ab648;
    --green-dark: #68a23a;
    --ink: #333b3f;
    --muted: #8d9396;
    --rule: #b5b5b5;
    --white: #ffffff;
    --hero-cream: #efe6cf;
    --hero-skin: #d99a94;
  }
  * { box-sizing: border-box; margin: 0; padding: 0; }
  html, body { width: 1200px; height: 1114px; overflow: hidden; background: var(--white); }
  body { font-family: "PT Sans", sans-serif; color: var(--ink); }
  .page { position: relative; width: 1200px; height: 1114px; overflow: hidden; }

  /* Header */
  .site-header {
    position: absolute; left: 0; top: 0; width: 1200px; height: 75px;
    background: var(--slate); border-top: 3px solid var(--green); z-index: 3;
  }
  .nav { position: absolute; top: 0; height: 72px; display: flex; align-items: center; gap: 32px; list-style: none; }
  .nav-left { left: 130px; }
  .nav-right { left: 769px; }
  .nav a {
    display: flex; align-items: center; gap: 5px; color: var(--white); text-decoration: none;
    font-family: "PT Sans Narrow", sans-serif; font-weight: 700; font-size: 15px; text-transform: uppercase;
  }
  .nav svg { width: 15px; height: 14px; fill: var(--white); }
  .brand-tab {
    position: absolute; left: 471px; top: 0; width: 258px; height: 151px; z-index: 4;
    background: var(--white); border-radius: 0 0 42px 42px;
    box-shadow: 0 3px 6px rgba(0,0,0,.25);
    display: flex; align-items: center; justify-content: center;
  }
  .brand-name {
    font-family: "PT Sans Narrow", sans-serif; font-size: 46px; font-weight: 400; color: var(--green);
    display: flex; align-items: center; gap: 10px;
  }
  .brand-dot { width: 14px; height: 14px; border-radius: 50%; background: var(--green); }

  /* Hero */
  .hero { position: absolute; left: 0; top: 75px; width: 1200px; height: 426px; }
  .hero-photo {
    position: absolute; inset: 0;
    background:
      radial-gradient(ellipse 260px 300px at 520px 260px, rgba(217,154,148,.95), rgba(217,154,148,0) 70%),
      radial-gradient(ellipse 420px 220px at 900px 200px, #e8d8a8, rgba(232,216,168,0) 75%),
      linear-gradient(180deg, #f1ead8 0%, #e9dfc4 55%, #ddd3c0 100%);
  }
  .hero-arrow {
    position: absolute; top: 160px; width: 68px; height: 68px; border-radius: 50%;
    background: rgba(90,90,90,.45); display: flex; align-items: center; justify-content: center;
  }
  .hero-arrow svg { width: 26px; height: 40px; fill: none; stroke: rgba(255,255,255,.8); stroke-width: 5; stroke-linecap: round; stroke-linejoin: round; }
  .hero-arrow.prev { left: 158px; }
  .hero-arrow.next { left: 974px; }
  .hero-title {
    position: absolute; left: 300px; top: 137px; width: 600px; text-align: center;
    font-family: "PT Sans Narrow", sans-serif; font-weight: 400; font-size: 48px; line-height: 57px; color: var(--white);
  }
  .hero-text {
    position: absolute; left: 362px; top: 264px; width: 476px; text-align: center;
    font-size: 15px; line-height: 20px; color: var(--white);
  }

  /* Main */
  .footprint-mark {
    position: absolute; left: 630px; top: 532px; width: 384px; height: 425px;
    background: radial-gradient(ellipse at 55% 55%, rgba(200,200,200,.22), rgba(200,200,200,0) 70%);
  }
  .welcome { position: absolute; left: 68px; top: 553px; width: 611px; }
  .eyebrow { font-size: 15px; color: var(--muted); }
  .welcome h1 {
    font-family: "PT Sans Narrow", sans-serif; font-weight: 400; font-size: 78px; line-height: 80px; color: var(--slate);
  }
  .section-rule { position: relative; height: 4px; background: var(--rule); margin-top: 6px; }
  .section-rule::before { content: ""; position: absolute; left: 0; top: 0; width: 90px; height: 4px; background: var(--green); }
  .welcome p { margin-top: 38px; font-size: 14.5px; line-height: 24px; }
  .btn-browse {
    position: absolute; left: 68px; top: 885px; width: 339px; height: 52px; border-radius: 26px;
    background: var(--green); border: 2px solid var(--green-dark); color: var(--white); text-decoration: none;
    font-family: "PT Sans Narrow", sans-serif; font-size: 26px; padding-left: 58px; line-height: 48px;
  }
  .btn-browse .chev {
    position: absolute; right: 8px; top: 6px; width: 36px; height: 36px; border-radius: 50%; background: var(--white);
    display: flex; align-items: center; justify-content: center;
  }
  .btn-browse .chev svg { width: 14px; height: 20px; fill: none; stroke: var(--green); stroke-width: 4.5; stroke-linecap: round; stroke-linejoin: round; }

  .newsletter { position: absolute; left: 792px; top: 596px; width: 340px; }
  .newsletter h2 { font-family: "PT Sans Narrow", sans-serif; font-weight: 400; font-size: 40px; line-height: 48px; color: var(--slate); }
  .signup {
    position: relative; margin-top: 44px; height: 52px; border-radius: 26px; background: var(--slate);
    border: 2px solid #1f292e;
  }
  .signup label { position: absolute; left: 28px; top: 14px; color: var(--white); font-style: italic; font-weight: 700; font-size: 15px; }
  .signup .ok {
    position: absolute; right: 5px; top: 5px; width: 38px; height: 38px; border-radius: 50%;
    background: var(--green); color: var(--white); font-style: italic; font-weight: 700; font-size: 16px;
    display: flex; align-items: center; justify-content: center;
  }
  .newsletter p { margin-top: 36px; font-size: 14.5px; line-height: 24px; }

  /* Footer */
  .site-footer {
    position: absolute; left: 0; top: 988px; width: 1200px; height: 126px;
    background: var(--slate);
  }
  .footer-brand {
    position: absolute; left: 68px; top: 42px; display: flex; align-items: center; gap: 8px;
    font-family: "PT Sans Narrow", sans-serif; font-size: 32px; color: var(--white);
  }
  .footer-brand .brand-dot { background: var(--white); width: 10px; height: 10px; }
  .social { position: absolute; left: 216px; top: 53px; display: flex; gap: 14px; list-style: none; }
  .social a { color: var(--white); text-decoration: none; font-size: 14px; font-weight: 700; }
  .legal {
    position: absolute; right: 68px; top: 54px; display: flex; gap: 20px; list-style: none;
    font-size: 16px; color: var(--white);
  }
  .legal a { color: var(--white); text-decoration: none; }
</style>
</head>
<body>
<div class="page">

  <header class="site-header">
    <ul class="nav nav-left">
      <li><a href="#"><svg viewBox="0 0 16 14"><circle cx="5" cy="4" r="3"/><circle cx="11.5" cy="4.5" r="2.5"/><path d="M0 13c0-4 2-6 5-6s5 2 5 6zM10 8c3 0 6 1 6 5h-5c0-2-0.5-3.5-1-5z"/></svg>About us</a></li>
      <li><a href="#"><svg viewBox="0 0 14 14"><path d="M3 0l3 3-2 2c1 2 3 4 5 5l2-2 3 3-2 3C6 14 0 8 0 3z"/></svg>Contact us</a></li>
      <li><a href="#"><svg viewBox="0 0 14 14"><circle cx="7" cy="4" r="3.5"/><path d="M1 14c0-4 2.5-6 6-6s6 2 6 6z"/></svg>Account</a></li>
    </ul>
    <ul class="nav nav-right">
      <li><a href="#"><svg viewBox="0 0 14 14"><rect x="0" y="1" width="6" height="5"/><rect x="8" y="1" width="6" height="5"/><rect x="0" y="8" width="6" height="5"/><rect x="8" y="8" width="6" height="5"/></svg>Categories</a></li>
      <li><a href="#"><svg viewBox="0 0 14 14"><path d="M0 0h6l8 8-6 6-8-8zM3 2.5a1 1 0 1 0 0.01 0z"/></svg>Products</a></li>
      <li><a href="#"><svg viewBox="0 0 16 14"><path d="M0 1h3l2 8h9l2-6H4.5"/><circle cx="6" cy="12" r="1.5"/><circle cx="13" cy="12" r="1.5"/></svg>Cart</a></li>
    </ul>
  </header>

  <a class="brand-tab" href="#"><span class="brand-name"><span class="brand-dot"></span>Dozelle</span></a>

  <section class="hero">
    <div class="hero-photo" role="img" aria-label="Photo of a baby's feet peeking out from under a soft cream blanket"></div>
    <a class="hero-arrow prev" href="#" aria-label="Previous slide"><svg viewBox="0 0 26 40"><path d="M19 5L6 20l13 15"/></svg></a>
    <a class="hero-arrow next" href="#" aria-label="Next slide"><svg viewBox="0 0 26 40"><path d="M7 5l13 15L7 35"/></svg></a>
    <h2 class="hero-title">lorem ipsum dolor sit amet, consectetur...</h2>
    <p class="hero-text">Lorem ipsum dolor sit amet, consectetur adipisicing elit, sed do eiusmod tempor incididunt ut labore et dolore magna aliqua. Ut enim ad minim veniam, quis nostrud exercitation ullamco laboris nisi ut aliquip ex ea commodo consequat.</p>
  </section>

  <div class="footprint-mark" role="img" aria-label="Faint baby footprint decoration"></div>

  <section class="welcome">
    <p class="eyebrow">Sed ut perspiciatis unde omnis iste..</p>
    <h1>Welcome</h1>
    <div class="section-rule"></div>
    <p>At vero eos et accusamus et iusto odio dignissimos ducimus qui blanditiis praesentium voluptatum deleniti atque corrupti quos dolores et quas molestias excepturi sint occaecati cupiditate non provident, similique sunt in culpa qui officia deserunt mollitia animi, id est laborum et dolorum fuga. Et harum quidem rerum facilis est et expedita distinctio. Nam libero tempore, cum soluta nobis est eligendi optio cumque nihil impedit quo minus id quod maxime placeat facere possimus, omnis voluptas assumenda est, omnis dolor repellendus.</p>
  </section>

  <a class="btn-browse" href="#">Browse Our Producs<span class="chev"><svg viewBox="0 0 14 20"><path d="M4 3l7 7-7 7"/></svg></span></a>

  <section class="newsletter">
    <h2>Sign up for Newsletter..</h2>
    <div class="section-rule"></div>
    <form class="signup">
      <label>Your e-mail address</label>
      <span class="ok">Ok</span>
    </form>
    <p>At vero eos et accusamus et iusto odio dignissimos ducimus qui blanditiis praesentium voluptatum deleniti atque corrupti...</p>
  </section>

  <footer class="site-footer">
    <div class="footer-brand"><span class="brand-dot"></span>Dozelle</div>
    <ul class="social">
      <li><a href="#">chatterly</a></li>
      <li><a href="#">chirpnet</a></li>
    </ul>
    <ul class="legal">
      <li>© 2013&nbsp; All Rights Reserved</li>
      <li>|</li>
      <li><a href="#">Privacy Policy</a></li>
      <li>|</li>
      <li><a href="#">Terms &amp; Conditons</a></li>
    </ul>
  </footer>

</div>
</body>
</html>
```